依頼詳細
おしゃれなイメージを希望しています。

掲載してもらいたい内容を載せています
宜しくお願いします。
①24時間営業
②11/6新規オープン(予定です。後日決定します)
③アクセスマップ(新しくできた『ふわりGATE』というモール内にコインランドリーが開店するということがわかるように)国道217号沿いでハナマルマートがあります。
④店内写真、屋外写真
⑤12/14まで全機種半額
洗濯乾燥8kg 900円→400円
洗濯乾燥15kg 1200円→600円
洗濯乾燥22kg 1500円→700円
洗濯のみ15kg 600円→300円
洗濯のみ22kg 900円→400円
洗濯のみ32kg 1100円→500円
乾燥のみ14kg 100円/10分→100円/20分
乾燥のみ25kg 100円/8分→100円/16分
シューズ用洗濯機 200円→100円
⑤洗濯機から乾燥機に移す面倒な手間いらずの全自動洗濯乾燥機を導入
⑥ふとんクリーニング店プロデュースなので羽毛布団、こたつ布団、毛布の洗濯も安心
⑦天然由来成分とEM(人体にも環境にもやさしい善玉菌の集合体)を配合した洗剤を使用しています。
記載項目
店名ロゴ(添付)、住所(大分市北松原215-3ふわりGATE C-204)、地図、店舗写真、店内写真
サイズ
A5
ページ数
両面
希望イメージ
シンプル 複雑
単色 カラフル
暗い 明るい
日常 高級
遊び心 厳粛
未来的 伝統的
女性的 男性的
希望する色
設定なし
納品ファイル
• イラストレーター形式 (.ai)
補足説明
店舗写真、店内写真は添付写真を当て込んでください。正式な写真は後日差し替えをお願いします。
新規のモール内の店舗ですので地図は大きめに表記をお願いします。
納品はアウトライン化したものとしていないものの両方お願いします。イラストレーターCS2で開けるようにしてください

訴求したい内容が一目でわかりやすい提案だったから

このたびはお忙しい中、多数のご提案をいただきありがとうございました。
今後も依頼していきますので機会がありましたらご提案くださいますようお願いします。
今後ともよろしくお願いします。

```html
<!DOCTYPE html>
<html lang="ja">
<head>
<meta charset="utf-8">
<title>Mofumo Laundry — NEW OPEN</title>
<link href="https://fonts.googleapis.com/css2?family=Fredoka:wght@600&family=Josefin+Sans:wght@400;600&family=M+PLUS+Rounded+1c:wght@500;700;800&display=swap" rel="stylesheet">
<style>
  :root {
    --teal: #3db7c6;
    --teal-deep: #2aa3b3;
    --ink: #1e3644;
    --paper: #ffffff;
  }
  html, body { margin: 0; padding: 0; overflow: hidden; background: var(--paper); }
  h1, h2, p { margin: 0; }
  .flyer {
    position: relative;
    width: 846px; height: 1200px;
    overflow: hidden;
    background: var(--paper);
    font-family: "M PLUS Rounded 1c", sans-serif;
    color: var(--ink);
  }
  .hero-photo {
    position: absolute; left: 0; top: 0; width: 846px; height: 336px;
    background: linear-gradient(180deg, #f1f2f0 0%, #e4e6e4 45%, #cfd2d0 62%, #7b5f49 72%, #5e4535 100%);
  }
  .brand {
    position: absolute; left: 0; top: 398px; width: 846px; height: 56px;
    display: flex; justify-content: center; align-items: center; gap: 14px;
    font-family: "Fredoka", sans-serif; font-weight: 600; font-size: 44px; line-height: 1;
    color: var(--teal-deep); letter-spacing: 1px;
  }
  .brand-mark { width: 38px; height: 38px; background: var(--ink); border-radius: 6px; }
  .date-line {
    position: absolute; left: 92px; top: 478px; width: 650px;
    display: flex; justify-content: space-between; align-items: baseline;
  }
  .open-date {
    font-family: "Josefin Sans", sans-serif; font-weight: 400; font-size: 56px; line-height: 1;
    color: var(--teal-deep); letter-spacing: 2px;
  }
  .open-date small { font-size: 32px; margin-left: 10px; }
  .mall-note { font-size: 24px; font-weight: 500; color: var(--ink); }
  .headline {
    position: absolute; left: 0; top: 562px; width: 846px; text-align: center;
    font-weight: 800; font-size: 116px; line-height: 1; letter-spacing: 2px;
    color: var(--teal);
    text-shadow: 4px 4px 0 var(--ink);
  }
  .offer {
    position: absolute; left: 90px; top: 708px; width: 560px; text-align: center;
    font-weight: 800; font-size: 76px; letter-spacing: 14px; line-height: 1;
    color: var(--ink);
  }
  .deadline-badge {
    position: absolute; left: 664px; top: 692px; width: 108px; height: 108px;
    border-radius: 50%; background: var(--teal); color: var(--paper);
    display: flex; flex-direction: column; align-items: center; justify-content: center;
    font-weight: 700; line-height: 1.15;
  }
  .deadline-badge .d { font-family: "Josefin Sans", sans-serif; font-size: 30px; }
  .deadline-badge .s { font-size: 17px; }
  .access {
    position: absolute; left: 0; top: 850px; width: 846px; height: 350px;
    background: var(--teal);
  }
  .access-title {
    position: absolute; left: 0; top: 18px; width: 846px; text-align: center;
    font-family: "Josefin Sans", sans-serif; font-weight: 400; font-size: 22px;
    letter-spacing: 4px; color: var(--paper);
  }
  .access-map {
    position: absolute; left: 56px; top: 54px; width: 326px; height: 230px;
    background: #f7f8f8;
  }
  .store-photo {
    position: absolute; left: 420px; top: 54px; width: 372px; height: 158px;
    background: linear-gradient(180deg, #c6ccd0 0%, #b9c0c4 35%, #3d3f42 55%, #55585b 75%, #8a8d8f 100%);
  }
  .store-info {
    position: absolute; left: 420px; top: 236px; width: 372px;
    display: flex; align-items: center; gap: 16px; color: var(--paper);
  }
  .hours { display: flex; align-items: center; gap: 6px; font-weight: 800; line-height: 1; }
  .hours .n { font-size: 56px; }
  .hours .u { font-size: 18px; line-height: 1.2; }
  .divider { width: 2px; height: 64px; background: var(--paper); }
  .address { font-size: 18px; font-weight: 700; line-height: 1.6; }
</style>
</head>
<body>
<main class="flyer">
  <div class="hero-photo" role="img" aria-label="店内写真：並んだ洗濯乾燥機と木目の床"></div>

  <div class="brand"><span>Mofumo</span><span class="brand-mark"></span><span>Laundry</span></div>

  <div class="date-line">
    <span class="open-date">11.6<small>Tue.</small></span>
    <span class="mall-note">「ふわりGATE」モール内</span>
  </div>

  <h1 class="headline">NEWOPEN</h1>
  <p class="offer">全機種半額</p>

  <div class="deadline-badge"><span class="d">12.14</span><span class="s">Fri.まで!</span></div>

  <section class="access">
    <h2 class="access-title">ACCESS MAP</h2>
    <div class="access-map" role="img" aria-label="アクセスマップ：国道217号沿い、ハナマルマート付近のふわりGATE内の店舗位置"></div>
    <div class="store-photo" role="img" aria-label="店舗外観写真"></div>
    <div class="store-info">
      <div class="hours"><span class="n">24</span><span class="u">時間<br>営業</span></div>
      <span class="divider"></span>
      <p class="address">大分市北松原215-3<br>ふわりGATE C-204</p>
    </div>
  </section>
</main>
</body>
</html>
```